Silverline Skills Institute

Our company needs a simple effective website with a clean design. We are working towards lowering the number of drownings that effect huge numbers each year. We will primarily link members to find education seminars, conferences and online material. With a forum to pose questions, have them answered by the community and moderated by staff members.

Target Market(s)

Swimming School Owners, Coaches, Parents and Community Groups

Industry/Entity Type

Education

Number of Pages Required

5+ page

Requirements
Must have
• A layout for all of the included pages. A good design for the forum. I will need to send this concept design to a coder for the final product.
Nice to have
• i would like to see an Olympic Swimming Pool incorporated into the options menu.

```html
<!DOCTYPE html>
<html lang="en">
<head>
<meta charset="utf-8">
<title>Silverline Skills Institute</title>
<link rel="stylesheet" href="https://fonts.googleapis.com/css2?family=Arvo:wght@400;700&family=Open+Sans:ital,wght@0,400;0,600;0,700;1,700&display=swap">
<style>
:root{
  --blue:#1c9ce0;
  --blue-dark:#0b66b0;
  --navy:#0e3a6b;
  --navy-deep:#0a2d55;
  --teal:#3cc8c0;
  --grey-cell:#e6e6e6;
  --grey-line:#cfcfcf;
  --text:#333;
  --muted:#666;
  --yellow:#f6c21b;
  --red:#d8262b;
  --white:#fff;
}
*{box-sizing:border-box;margin:0;padding:0}
html,body{width:1200px;height:2717px;overflow:hidden}
body{position:relative;background:var(--white);font-family:"Open Sans",Arial,sans-serif;color:var(--text)}

/* header */
.site-header{position:absolute;left:0;top:0;width:1200px;height:95px;background:var(--white)}
.brand{position:absolute;left:158px;top:6px;width:88px;height:88px;border-radius:50%;border:4px solid var(--blue);display:flex;align-items:center;justify-content:center;font:700 26px "Open Sans",sans-serif;color:var(--blue)}
.main-nav{position:absolute;left:376px;top:39px;width:560px;height:30px}
.main-nav a{position:absolute;top:0;white-space:nowrap;font:600 11px "Open Sans",sans-serif;color:#444;text-decoration:none}
.main-nav a.active{color:var(--blue)}
.main-nav a.active::after{content:"";position:absolute;left:0;right:0;top:21px;height:2px;background:var(--teal)}
.login-btn{position:absolute;left:942px;top:30px;width:95px;height:33px;background:var(--teal);color:#fff;font:700 12px "Open Sans",sans-serif;display:flex;align-items:center;justify-content:center}

/* hero */
.hero{position:absolute;left:0;top:95px;width:1200px;height:460px;background:linear-gradient(110deg,#4a8fb5 0%,#c9a98a 30%,#6d8fa6 55%,#3b6f98 80%,#9fb5c4 100%)}
.hero-title{position:absolute;left:281px;top:154px;width:643px;height:107px;background:rgba(20,40,110,.72);color:#fff;font:700 32px/44px "Arvo",serif;text-align:center;white-space:nowrap;display:flex;flex-direction:column;justify-content:center}
.dots{position:absolute;display:flex;gap:6px}
.dots span{width:9px;height:9px;border-radius:50%;background:#cfe3f3;border:1px solid #6aa6d3}
.dots span.on{background:var(--blue)}

/* welcome */
.welcome{position:absolute;left:215px;top:509px;width:781px;height:272px;background:var(--white);box-shadow:0 1px 6px rgba(0,0,0,.15);text-align:center;padding:30px 22px 0}
.welcome h1{font:700 25px "Open Sans",sans-serif;color:var(--blue)}
.welcome h2{font:400 19px "Arvo",serif;color:#222;margin-top:4px}
.welcome p{font-size:10.5px;line-height:21px;color:var(--muted);margin-top:10px}
.partners{position:absolute;left:158px;top:790px;width:884px;height:110px;display:flex}
.partner{flex:1;display:flex;align-items:center;justify-content:center;border-right:1px solid #ddd}
.partner:last-child{border-right:0}

/* involved */
.involved{position:absolute;left:0;top:928px;width:1200px;height:306px;background:linear-gradient(180deg,#1f9fe3,#1786cc);color:#fff;text-align:center}
.involved h2{font:700 27px "Arvo",serif;margin-top:34px}
.involved p{font-size:11px;line-height:21px;width:880px;margin:14px auto 0}
.ghost-btn{display:inline-block;margin-top:20px;width:112px;height:30px;border:1px solid #fff;background:var(--navy);font:700 11px/28px "Open Sans",sans-serif}

/* events */
.events-head{position:absolute;left:0;top:1258px;width:1200px;text-align:center}
.events-head h2{font:700 29px "Arvo",serif;color:#111}
.events-head p{font:400 19px "Arvo",serif;color:#333;margin-top:2px}
.calendar{position:absolute;left:158px;top:1336px;width:884px;border-collapse:collapse;table-layout:fixed}
.cal-month{background:var(--blue);color:#fff;font:700 12px "Open Sans",sans-serif;height:38px;text-align:center}
.calendar th.day{background:var(--navy);color:#fff;font:600 12px "Open Sans",sans-serif;height:36px;border:1px solid #0a2f57}
.calendar td{background:var(--grey-cell);border:1px solid var(--grey-line);height:122px;vertical-align:top;padding:8px;font-size:12px;color:#222}
.event-link{display:block;color:var(--red);font:600 11px/15px "Open Sans",sans-serif;margin-top:10px}
.event-pop{position:absolute;left:550px;top:1743px;width:193px;height:86px;background:var(--yellow);padding:8px 10px;font-size:10px;line-height:20px;color:#222}
.event-pop b{font-weight:700}
.event-pop .more{color:var(--red);font-weight:700}
.apply-btn{position:absolute;left:516px;top:2049px;width:165px;height:30px;background:var(--teal);color:#fff;font:700 11px/30px "Open Sans",sans-serif;text-align:center}

/* client */
.client{position:absolute;left:0;top:2117px;width:1200px;height:324px;background:linear-gradient(180deg,#0e2f58 0%,#1a4f7f 50%,#0b2847 100%);text-align:center;color:#fff}
.client h2{font:700 27px "Arvo",serif;color:var(--blue);margin-top:26px;line-height:30px}
.client h3{font:400 19px "Arvo",serif;color:#fff;line-height:22px}
.client p{width:780px;margin:14px auto 0;font-size:10.5px;line-height:21px}
.quote{position:absolute;font:700 60px/1 "Arvo",serif;color:var(--yellow)}
.client .who{font:italic 700 15px "Open Sans",sans-serif;color:var(--yellow);margin-top:12px}
.client .role{font-size:12px;margin-top:4px}

/* quick links */
.quick-links{position:absolute;left:0;top:2441px;width:1200px;height:99px;background:var(--blue);display:flex;justify-content:center}
.quick-link{width:300px;display:flex;align-items:center;justify-content:center;gap:10px;color:#fff;font:600 19px "Open Sans",sans-serif;border-right:1px solid rgba(255,255,255,.35)}
.quick-link:last-child{border-right:0}

/* footer */
.site-footer{position:absolute;left:0;top:2540px;width:1200px;height:177px;background:var(--navy-deep);color:#fff}
.footer-brand{position:absolute;left:158px;top:18px;width:96px;height:96px;border-radius:50%;background:#fff;border:4px solid var(--blue);color:var(--blue);font:700 26px "Open Sans",sans-serif;display:flex;align-items:center;justify-content:center}
.footer-address{position:absolute;left:260px;top:52px;font:600 11px/18px "Open Sans",sans-serif}
.social{position:absolute;left:783px;top:50px;display:flex;gap:14px}
.social span{width:30px;height:30px;border-radius:50%;background:#3a7cc0}
.footer-nav{position:absolute;left:160px;top:144px;display:flex;gap:14px;font:600 10px "Open Sans",sans-serif}
.copyright{position:absolute;left:858px;top:144px;font-size:9px;color:#c8d6e6}
</style>
</head>
<body>

<header class="site-header">
  <div class="brand">SSI</div>
  <nav class="main-nav">
    <a class="active" style="left:0">HOME</a>
    <a style="left:45px">ABOUT US</a>
    <a style="left:115px">COMMUNITY</a>
    <a style="left:195px">EVENTS</a>
    <a style="left:251px">WHY GET INVOLVED</a>
    <a style="left:369px">BECOME CERTIFIED</a>
    <a style="left:487px">CONTACT US</a>
  </nav>
  <div class="login-btn">LOG IN</div>
</header>

<section class="hero" role="img" aria-label="Swim instructor teaching children at the edge of an outdoor pool">
  <div class="hero-title"><span>Providing High-Quality Learning</span><span>Opportunities for SSI</span></div>
  <div class="dots" style="left:582px;top:398px"><span class="on"></span><span></span><span></span></div>
</section>

<section class="welcome">
  <h1>Welcome to Bluewater Swim Centre</h1>
  <h2>Water Safety and Aquatic Education</h2>
  <p>Each year globally there are 372 000 people drowning everyday, from young children to victims of flood. According to a 2007 report released by Safe Children Network, as many as 30,000 children between 0 and 14 years old die by drowning each year. That accounts for up to 60 percent of the annual 50,000 accidental child deaths, and the figures are climbing. This tally isn't frightening enough: think of the non drownings that lead to permanent brain damage and disability. Spreading the message of water safety and education is important to reduce this number and give everyone a fighting chance. There are many simple life saving skills and tips that can be spread with very little cost. Barriers on waterways, safe areas to leave children away from water, education in swimming, training in lifesaving techniques and most importantly education on the associated risks to young children around water.</p>
</section>

<div class="partners">
  <div class="partner"><svg width="62" height="62"><circle cx="31" cy="31" r="29" fill="#f2b632"/></svg></div>
  <div class="partner"><svg width="110" height="54"><rect width="110" height="54" rx="6" fill="#2a72c4"/></svg></div>
  <div class="partner"><svg width="62" height="62"><rect width="62" height="62" rx="8" fill="#8a5bc4"/></svg></div>
  <div class="partner"><svg width="150" height="44"><rect width="150" height="44" rx="22" fill="#222"/></svg></div>
</div>

<section class="involved" role="img" aria-label="Blue band with a faint photo of a child swimming underwater">
  <h2>Why Become Involved</h2>
  <p>The best way to provide education is in a safe controlled environment. Running your own facility is a rewarding lifelong move into business. Providing a community service with an opportunity to work with a passionate and driven community. Become a leader in educating children to be safe around water.<br>Creating a purpose built facility can be tough. Having a good heart is a great start, but misinformation can be just as dangerous as no information.<br>Your good intentions need to be directed effectively.<br>The most important asset is great coaches and a top notch pool. Luckily the industry has been around for a long time and has produced some excellent models that you can follow.<br>With many countries having turn key consulting to help you on your way.</p>
  <div class="ghost-btn">FIND OUT MORE</div>
</section>

<div class="events-head">
  <h2>UPCOMING EVENTS</h2>
  <p>For More Information On Calendar Events</p>
</div>

<table class="calendar">
  <tr><th class="cal-month" colspan="7">&#9664;&nbsp; MARCH 2016 &nbsp;&#9654;</th></tr>
  <tr><th class="day">MONDAY</th><th class="day">TUESDAY</th><th class="day">WEDNESDAY</th><th class="day">THURSDAY</th><th class="day">FRIDAY</th><th class="day">SATURDAY</th><th class="day">SUNDAY</th></tr>
  <tr><td></td><td>1</td><td>2</td><td>3</td><td>4</td><td>5</td><td>6</td></tr>
  <tr><td>7</td><td>8</td><td>9</td><td>10</td><td>11</td><td>12</td><td>13</td></tr>
  <tr><td>14</td><td>15</td><td>16</td><td>17<span class="event-link">Riverside<br>Community<br>Gathering</span></td><td>18</td><td>19</td><td>20</td></tr>
  <tr><td>21</td><td>22</td><td>23</td><td>24</td><td>25</td><td>26</td><td>27</td></tr>
  <tr><td>28</td><td>29</td><td>30</td><td>31</td><td></td><td></td><td></td></tr>
</table>
<div class="event-pop"><b>EVENT TIME : 9 : 00 AM TO 7 : 00 PM</b><br>Riverside Community Gathering<br><span class="more">VIEW EVENT DETAILS &rsaquo;</span></div>
<div class="apply-btn">CLICK THE LINK TO APPLY</div>

<section class="client" role="img" aria-label="Dark underwater photo of a swimmer behind the testimonial">
  <h2>OUR CLIENT</h2>
  <h3>SUCCESSES</h3>
  <div class="quote" style="left:168px;top:106px">&ldquo;</div>
  <div class="quote" style="left:1000px;top:186px">&rdquo;</div>
  <p>Lorem ipsum dolor sit amet, consectetur adipiscing elit, sed do eiusmod tempor incididunt ut labore et dolore magna aliqua. Ut enim ad minim veniam, quis nostrud exercitation ullamco laboris nisi ut aliquip ex ea commodo consequat. Duis aute irure dolor in reprehenderit in voluptate velit esse cillum dolore eu fugiat nulla pariatur. Excepteur sint occaecat cupidatat non proident, sunt in culpa qui officia deserunt mollit anim id est laborum. Sed ut perspiciatis unde omnis iste natus error sit voluptatem accusantium doloremque laudantium, totam rem aperiam, eaque ipsa quae ab illo inventore veritatis et quasi architecto beatae vitae dicta sunt explicabo. Nemo enim ipsam voluptatem quia voluptas sit aspernatur aut odit aut fugit, sed quia consequuntur magni dolores eos qui ratione voluptatem sequi nesciunt.</p>
  <div class="who">Dana L. Whitmore</div>
  <div class="role">Chemical Engineer</div>
  <div class="dots" style="left:582px;top:290px"><span class="on"></span><span></span><span></span></div>
</section>

<nav class="quick-links">
  <div class="quick-link">
    <svg width="26" height="34" viewBox="0 0 26 34"><path d="M4 10a9 9 0 1 1 13 8c-3 2-4 3-4 7" fill="none" stroke="#fff" stroke-width="4" stroke-linecap="round"/><circle cx="13" cy="31" r="2.6" fill="#fff"/></svg>INQUIRE
  </div>
  <div class="quick-link">
    <svg width="28" height="28" viewBox="0 0 28 28"><path d="M4 24l2-7L19 4l5 5L11 22z" fill="none" stroke="#fff" stroke-width="2.5" stroke-linejoin="round"/><path d="M16 7l5 5" stroke="#fff" stroke-width="2.5"/></svg>APPLY
  </div>
  <div class="quick-link">
    <svg width="34" height="28" viewBox="0 0 34 28"><circle cx="17" cy="7" r="5" fill="#fff"/><circle cx="6" cy="14" r="4" fill="#fff"/><circle cx="28" cy="14" r="4" fill="#fff"/><path d="M10 27a7 7 0 0 1 14 0z" fill="#fff"/><path d="M0 27a6 6 0 0 1 11-3v3z M34 27a6 6 0 0 0-11-3v3z" fill="#fff"/></svg>COMMUNITY
  </div>
</nav>

<footer class="site-footer">
  <div class="footer-brand">SSI</div>
  <div class="footer-address">218 Harbor Lane<br>Fairview, MO 65000</div>
  <div class="social"><span></span><span></span><span></span><span></span><span></span><span></span></div>
  <nav class="footer-nav"><span>HOME</span><span>ABOUT US</span><span>COMMUNITY</span><span>EVENTS</span><span>WHY GET INVOLVED</span><span>BECOME CERTIFIED</span><span>CONTACT US</span></nav>
  <div class="copyright">Copyright © 2016 SSI. All Rights Reserved.</div>
</footer>

</body>
</html>
```